依頼詳細
PC版のTOPページと下層1ページのデザイン制作をお願いいたします。
TOPページメイン部分に埋め込み用の動画、サイトマップ、依頼内容詳細.txtをご確認いただき、動画のテイスト(方眼紙やフォントなど)を参考にシンプルで見やすいデザインで制作いただきたいです。
スムーズな連絡と軽微な修正にご対応いただける方へご依頼をさせていただきたいです。
ターゲットは建築資材・家具建具資材・住設機器などを必要とする建築会社様、家具・建具製造会社様などです。
ページ数
2ページ
希望イメージ
シンプル 複雑
単色 カラフル
暗い 明るい
日常 高級
遊び心 厳粛
未来的 伝統的
女性的 男性的
希望する色
青系、茶系、グレー系
納品ファイル
• イラストレーター形式 (.ai)
補足説明
納品ファイルはXDも可です。
-
■ 選んだ理由

動画とのイメージが合っており選ばせていただきました。

■ 提案者全員のお礼・コメント

たくさんのご提案をいただきありがとうございました。
また機会がございましたらよろしくお願いいたします。

```html
<!DOCTYPE html>
<html lang="ja">
<head>
<meta charset="utf-8">
<title>MINATO KENZAI | CUSTOMER</title>
<link href="https://fonts.googleapis.com/css2?family=Noto+Sans+JP:wght@400;500;700;900&family=Montserrat:wght@500;700;800&display=swap" rel="stylesheet">
<style>
:root{
  --blue:#1e73c8;
  --blue-light:#3fa3e0;
  --navy:#0e2a4a;
  --teal:#2bb3c8;
  --ink:#222;
  --text:#555;
  --muted:#999;
  --line:#e2e2e2;
  --footer:#f3f3f3;
  --white:#fff;
}
*{box-sizing:border-box;margin:0;padding:0}
html,body{width:1200px;height:3188px;overflow:hidden;background:var(--white)}
body{font-family:"Noto Sans JP",sans-serif;color:var(--ink);position:relative}
.en{font-family:"Montserrat",sans-serif}

/* header + hero */
.hero{position:absolute;left:0;top:0;width:1200px;height:590px;
  background:linear-gradient(180deg,#d9dcdd 0%,#c7c9c6 45%,#b9bdb4 75%,#8e9a86 100%)}
.hero::after{content:"";position:absolute;inset:0;background:rgba(20,30,40,.18)}
.site-header{position:absolute;left:0;top:0;width:1200px;height:80px;z-index:2;display:flex;align-items:center;padding:0 0 0 40px}
.brand{font-weight:700;font-size:26px;color:var(--white);letter-spacing:1px}
.gnav{margin-left:auto;display:flex;align-items:center;height:80px}
.gnav a{display:block;text-align:center;color:var(--white);text-decoration:none;padding:0 13px;line-height:1.2}
.gnav a .en{font-size:14px;font-weight:700;display:block}
.gnav a .ja{font-size:10px;display:block;margin-top:3px}
.gnav a.nav-contact{background:var(--blue);height:80px;display:flex;flex-direction:column;justify-content:center;padding:0 24px;margin-left:6px}
.hero-title{position:absolute;left:40px;top:200px;z-index:2;color:var(--white)}
.hero-title .en{font-size:76px;font-weight:800;letter-spacing:2px;line-height:1}
.hero-title .ja{font-size:28px;font-weight:700;color:var(--blue-light);margin-top:4px}

/* breadcrumb */
.breadcrumb{position:absolute;left:88px;top:640px;font-size:13px;color:var(--text);display:flex;gap:10px;align-items:center}
.breadcrumb svg{width:14px;height:14px}

/* article */
.article{position:absolute;left:88px;top:730px;width:700px}
.article h1{font-size:26px;font-weight:700;line-height:1.4}
.meta{font-size:12px;color:var(--text);margin-top:20px}
.photo{display:block;width:700px}
.main-photo{height:390px;margin-top:20px;background:linear-gradient(135deg,#ece9e4 0%,#cfc5b8 40%,#8d7b6a 70%,#c9cdd0 100%)}
.h2{margin-top:20px;background:var(--blue);color:var(--white);font-size:21px;font-weight:700;padding:14px 20px;border-left:6px solid var(--navy)}
.body-text{font-size:14px;color:var(--text);line-height:1.9;margin-top:18px;letter-spacing:.5px}
.h3{margin-top:30px;font-size:19px;font-weight:700;padding:6px 0 6px 16px;border-left:5px solid var(--blue)}
.h4{margin-top:30px;font-size:18px;font-weight:700;padding:8px 0 8px 30px;border-bottom:1px solid var(--line)}
.media-block{display:flex;gap:24px;margin-top:34px;align-items:flex-start}
.media-block .col{flex:1}
.media-block .h3{margin-top:0;line-height:1.5}
.side-photo{width:340px;height:220px;flex:none;background:linear-gradient(135deg,#eef0ec 0%,#c9d4c0 40%,#7f9b6d 75%,#dfe3df 100%)}
.pager{display:flex;justify-content:space-between;margin-top:50px}
.pager a{display:flex;align-items:center;gap:10px;border:1px solid #bbb;border-radius:22px;padding:9px 22px;font-size:13px;color:var(--text);text-decoration:none}

/* sidebar */
.sidebar{position:absolute;left:872px;top:620px;width:240px;background:var(--white);box-shadow:0 4px 18px rgba(0,0,0,.12);padding:30px 22px 30px}
.sidebar h2{font-size:19px;font-weight:700;padding-bottom:14px;border-bottom:2px solid var(--blue)}
.side-list{list-style:none}
.side-list li{padding:14px 0;border-bottom:1px solid var(--line)}
.side-list .t{font-size:13px;font-weight:500;line-height:1.5}
.side-list .d{font-size:11px;color:var(--muted);margin-top:4px}
.side-btn{display:flex;justify-content:center;align-items:center;gap:10px;margin:26px auto 0;width:150px;border:1px solid var(--blue);color:var(--blue);font-size:12px;padding:10px 0;text-decoration:none}

/* contact band */
.contact-band{position:absolute;left:0;top:2370px;width:1200px;height:390px;
  background:linear-gradient(100deg,var(--navy) 0%,#174e78 45%,var(--teal) 100%);color:var(--white);text-align:center}
.contact-band h2{font-size:58px;font-weight:800;padding-top:80px;letter-spacing:2px;line-height:1.1}
.contact-band p{font-size:16px;margin-top:26px}
.contact-btn{display:inline-flex;align-items:center;gap:18px;margin-top:40px;border:1px solid var(--white);color:var(--white);text-decoration:none;font-size:13px;padding:14px 44px}

/* footer */
.site-footer{position:absolute;left:0;top:2760px;width:1200px;height:428px;background:var(--footer)}
.footer-brand{position:absolute;left:88px;top:50px;font-size:30px;font-weight:700}
.footer-info{position:absolute;left:88px;top:130px;font-size:13px;line-height:1.8;color:var(--text)}
.footer-info .gap{margin-top:18px}
.fnav{position:absolute;left:470px;top:130px;display:grid;grid-template-columns:repeat(5,130px);row-gap:46px;font-size:12px;color:var(--ink)}
.fnav ul{list-style:none}
.fnav li.sub{font-size:10px;color:var(--text);margin-top:6px;padding-left:10px}
.copyright{position:absolute;left:0;bottom:24px;width:100%;text-align:center;font-size:10px;color:var(--muted)}
</style>
</head>
<body>

<div class="hero" role="img" aria-label="新築住宅の前で家族が並ぶ写真"></div>
<header class="site-header">
  <div class="brand">MINATO KENZAI</div>
  <nav class="gnav">
    <a href="#"><span class="en">ABOUT</span><span class="ja">会社概要</span></a>
    <a href="#"><span class="en">SERVICE</span><span class="ja">事業内容</span></a>
    <a href="#"><span class="en">PRODUCT</span><span class="ja">取扱商品</span></a>
    <a href="#"><span class="en">CUSTOMER</span><span class="ja">お施主様へ</span></a>
    <a href="#"><span class="en">PARTNER</span><span class="ja">お取引先様へ</span></a>
    <a href="#"><span class="en">NEWS</span><span class="ja">新着情報</span></a>
    <a href="#"><span class="en">RECRUIT</span><span class="ja">採用情報</span></a>
    <a href="#" class="nav-contact"><span class="en">CONTACT</span><span class="ja">お問い合わせ</span></a>
  </nav>
</header>
<div class="hero-title">
  <div class="en">CUSTOMER</div>
  <div class="ja">お施主様へ</div>
</div>

<div class="breadcrumb">
  <svg viewBox="0 0 14 14"><path d="M1 7 7 1l6 6v6H9V9H5v4H1z" fill="#333"/></svg>
  <span>ホーム</span><span>&gt;</span><span>お施主様お役立ち情報一覧</span><span>&gt;</span><span>お施主様お役立ち情報投稿タイトル</span>
</div>

<main class="article">
  <h1>お施主様お役立ち情報投稿タイトル</h1>
  <div class="meta">投稿日：2024.10.10　更新日：2024.10.10</div>
  <div class="photo main-photo" role="img" aria-label="明るいシステムキッチンの写真"></div>

  <h2 class="h2">H2見出しタイトルH2見出しタイトルH2見出しタイトル</h2>
  <p class="body-text">ここにテキストが入ります。ここにテキストが入ります。ここにテキストが入ります。ここにテキストが入ります。ここにテキストが入ります。ここにテキストが入ります。ここにテキストが入ります。ここにテキストが入ります。ここにテキストが入ります。ここにテキストが入ります。ここにテキストが入ります。ここにテキストが入ります。ここにテキストが入ります。ここにテキストが入ります。ここにテキストが入ります。ここにテキストが入ります。</p>

  <h3 class="h3">H3見出しタイトルH3見出しタイトルH3見出しタイトル</h3>
  <p class="body-text">ここにテキストが入ります。ここにテキストが入ります。ここにテキストが入ります。ここにテキストが入ります。ここにテキストが入ります。ここにテキストが入ります。ここにテキストが入ります。ここにテキストが入ります。ここにテキストが入ります。ここにテキストが入ります。ここにテキストが入ります。ここにテキストが入ります。</p>

  <h4 class="h4">H4見出しタイトルH4見出しタイトルH4見出しタイトル</h4>
  <p class="body-text">ここにテキストが入ります。ここにテキストが入ります。ここにテキストが入ります。ここにテキストが入ります。ここにテキストが入ります。ここにテキストが入ります。ここにテキストが入ります。ここにテキストが入ります。ここにテキストが入ります。ここにテキストが入ります。ここにテキストが入ります。ここにテキストが入ります。ここにテキストが入ります。ここにテキストが入ります。ここにテキストが入ります。ここにテキストが入ります。ここにテキストが入ります。ここにテキストが入ります。</p>

  <div class="media-block">
    <div class="col">
      <h3 class="h3">H3見出しタイトルH3タイトルH3タイトルH3タイトルH3見出しタイトルH3タイトル</h3>
      <p class="body-text">ここにテキストが入ります。ここにテキストが入ります。ここにテキストが入ります。ここにテキストが入ります。ここにテキストが入ります。ここにテキストが入ります。</p>
    </div>
    <div class="side-photo" role="img" aria-label="大きな窓から緑が見えるリビングの写真"></div>
  </div>

  <nav class="pager">
    <a href="#"><svg width="8" height="12" viewBox="0 0 8 12"><path d="M7 1 2 6l5 5" fill="none" stroke="#555" stroke-width="1.5"/></svg><span class="en">PREV</span></a>
    <a href="#"><span class="en">NEXT</span><svg width="8" height="12" viewBox="0 0 8 12"><path d="m1 1 5 5-5 5" fill="none" stroke="#555" stroke-width="1.5"/></svg></a>
  </nav>
</main>

<aside class="sidebar">
  <h2>お役立ち情報一覧</h2>
  <ul class="side-list">
    <li><div class="t">お施主様お役立ち情報タイトル</div><div class="d">2024.10.10</div></li>
    <li><div class="t">お施主様お役立ち情報タイトル</div><div class="d">2024.10.10</div></li>
    <li><div class="t">お施主様お役立ち情報タイトル</div><div class="d">2024.10.10</div></li>
    <li><div class="t">お施主様お役立ち情報タイトル</div><div class="d">2024.10.10</div></li>
    <li><div class="t">お施主様お役立ち情報タイトル</div><div class="d">2024.10.10</div></li>
    <li><div class="t">お施主様お役立ち情報タイトル</div><div class="d">2024.10.10</div></li>
    <li><div class="t">お施主様お役立ち情報タイトル</div><div class="d">2024.10.10</div></li>
  </ul>
  <a href="#" class="side-btn">お役立ち情報一覧<svg width="7" height="10" viewBox="0 0 7 10"><path d="m1 1 4 4-4 4" fill="none" stroke="#1e73c8" stroke-width="1.5"/></svg></a>
</aside>

<section class="contact-band">
  <h2 class="en">CONTACT</h2>
  <p>お見積もり・ご相談・ご依頼などお気軽にお問い合わせください。</p>
  <a href="#" class="contact-btn">お問い合わせページ<svg width="20" height="8" viewBox="0 0 20 8"><path d="M0 7h18l-5-5" fill="none" stroke="#fff" stroke-width="1.2"/></svg></a>
</section>

<footer class="site-footer">
  <div class="footer-brand">MINATO KENZAI</div>
  <div class="footer-info">
    <div>〒000-0000</div>
    <div>北海道札幌市〇〇区〇〇町1-2-3</div>
    <div class="gap">TEL：012-345-6789</div>
    <div>FAX：012-345-6780</div>
    <div>営業時間：8:30〜17:30（土・日・祝休）</div>
  </div>
  <div class="fnav">
    <ul><li>TOPページ</li></ul>
    <ul><li>会社概要</li></ul>
    <ul><li>事業内容</li></ul>
    <ul><li>取扱商品</li></ul>
    <ul><li>お施主様へ</li><li class="sub">・お役立ち情報一覧</li><li class="sub">・施工事例一覧</li></ul>
    <ul><li>お取引先様へ</li><li class="sub">・お取引について</li><li class="sub">・資材のご案内</li><li class="sub">・よくある質問</li><li class="sub">・納品エリア</li></ul>
    <ul><li>新着情報</li></ul>
    <ul><li>採用情報</li></ul>
    <ul><li>お問い合わせ</li></ul>
    <ul><li>プライバシーポリシー</li></ul>
  </div>
  <div class="copyright">Copyright © MINATO KENZAI All rights reserved.</div>
</footer>

</body>
</html>
```